Seven nights at the harbour

Creation of the cover for the book: "Sept nuits sur le quai du port" with the joined photo of a 70 years old lady.
Title: "Seven nights along the old harbour"
Author: "Mireille Vaston"
Publisher: "Editions Morvane" (should be at the bottom of the page)
Format: 14 x 20.5 cm
The story: A senior lady (70 years old), divorced, with a beautiful face, still wants to seduce, even young men.
We found the perfect photo for the woman. We would like to ask you to make a modern cover from it.
Besoin de quelques jours pour choisir un design
Target Market(s)
Novels reader (adults)
Industry/Entity Type
book

```html
<!DOCTYPE html>
<html lang="en">
<head>
<meta charset="utf-8">
<title>Seven nights at the harbour — cover</title>
<link rel="stylesheet" href="https://fonts.googleapis.com/css2?family=Federo&family=Poppins:wght@500;600;700&display=swap">
<style>
  :root {
    --stage: #d3d3d3;
    --paper: #ffffff;
    --ink: #111111;
    --photo-light: #6e6e6e;
    --photo-mid: #4a4a4a;
    --photo-dark: #2a2a2a;
    --skin: #7a4a3a;
    --digit-red: #6b0000;
    --shade: rgba(0, 0, 0, 0.45);
    --accent-red: #ff0000;
    --text-light: #ffffff;
  }
  * { margin: 0; padding: 0; box-sizing: border-box; }
  html, body {
    width: 1200px; height: 1000px; overflow: hidden;
    background: var(--stage);
  }
  .cover {
    position: absolute; left: 278px; top: 29px;
    width: 643px; height: 942px;
    background: var(--paper);
    box-shadow: 0 6px 24px rgba(0,0,0,0.25);
    overflow: hidden;
  }
  .author-band {
    position: absolute; left: 0; top: 0; width: 100%; height: 46px;
    background: var(--paper);
    display: flex; align-items: center; justify-content: center;
    font-family: "Poppins", sans-serif; font-weight: 700;
    font-size: 22px; letter-spacing: 0.5px; color: var(--ink);
  }
  .portrait {
    position: absolute; left: 0; top: 46px; width: 100%; height: 896px;
    background:
      radial-gradient(ellipse 32% 30% at 48% 48%, var(--skin) 0%, rgba(122,74,58,0) 100%),
      linear-gradient(160deg, var(--photo-light) 0%, var(--photo-mid) 45%, var(--photo-dark) 100%);
  }
  .numeral {
    position: absolute; left: 0; top: 46px; width: 643px; height: 896px;
  }
  .subtitle {
    position: absolute; left: 0; width: 100%; top: 82px;
    text-align: center;
    font-family: "Poppins", sans-serif; font-weight: 500;
    font-size: 21px; color: var(--text-light);
  }
  .title {
    position: absolute; left: 0; width: 100%;
    text-align: center;
    font-family: "Federo", sans-serif; color: var(--text-light);
    line-height: 1; white-space: nowrap;
  }
  .title-line-1 { top: 652px; font-size: 70px; }
  .title-line-2 { top: 744px; font-size: 54px; }
  .title-line-3 { top: 818px; font-size: 54px; }
  .title-accent { color: var(--accent-red); }
  .publisher {
    position: absolute; left: 0; width: 100%; top: 893px;
    text-align: center;
    font-family: "Poppins", sans-serif; font-weight: 600;
    font-size: 21px; color: var(--text-light);
  }
</style>
</head>
<body>
  <main class="cover">
    <header class="author-band">MIREILLE VASTON</header>

    <div class="portrait" role="img" aria-label="Close-up photo of a seventy-year-old woman with long grey hair blown across her face"></div>

    <svg class="numeral" viewBox="0 0 643 896" aria-hidden="true">
      <rect x="322" y="0" width="321" height="896" fill="var(--shade)"/>
      <path d="M 0 40 L 643 40 L 643 120 Q 420 420 330 896 L 220 896 Q 300 440 520 120 L 0 120 Z"
            fill="var(--digit-red)" opacity="0.85"/>
    </svg>

    <p class="subtitle">SEPT NUITS SUR LE QUAI DU PORT</p>

    <h1>
      <span class="title title-line-1">SEVEN NIGHTS</span>
      <span class="title title-line-2">ALONG THE</span>
      <span class="title title-line-3">OLD <span class="title-accent">HARBOUR</span></span>
    </h1>

    <footer class="publisher">EDITIONS MORVANE</footer>
  </main>
</body>
</html>
```